Stanbrook Fire Services Pty Ltd

We need business cards for a company based in Perth, we install, service and maintain fire equipment.
On the front we want a great design with our logo and a small spot for our full company name, general company email address and office number. On the back we need space for our name, title, mobile number and email address on the back.

Target Market(s)

Facility managers and commercial/industrial building owners/occupiers.

Contact Information for Business Card

Font styles to use
Sans Serif

Requirements
Must have
• Please only submit 5 of your best samples.
Darker tones are preferred.
Nice to have
• We want to use, black, red and grey. Keep it modern and clean.
I've attached the company logo and a sample of a boarder we use on our emergency plans.
Should not have
• No preference. Let the designer choose.

```html
<!DOCTYPE html>
<html lang="en">
<head>
<meta charset="utf-8">
<title>Stanbrook Fire Services – Business Cards</title>
<link href="https://fonts.googleapis.com/css2?family=Montserrat:wght@700&family=Roboto:wght@400&display=swap" rel="stylesheet">
<style>
  :root {
    --backdrop: #e6e3de;
    --card: #1b1b1d;
    --red: #e3212b;
    --grey: #8a8a8c;
    --divider: #4a4a4d;
    --text: #f2f2f2;
  }
  html, body {
    margin: 0;
    width: 1200px;
    height: 859px;
    overflow: hidden;
    background: var(--backdrop);
  }
  .card {
    position: absolute;
    top: 288px;
    width: 502px;
    height: 286px;
    background: var(--card);
    box-shadow: 0 6px 16px rgba(0,0,0,0.25);
  }
  .card--person { left: 59px; }
  .card--company { left: 639px; }
  .tab {
    position: absolute;
    width: 78px;
    height: 10px;
    background: var(--red);
  }
  .tab--top { top: 0; left: 0; }
  .tab--bottom { bottom: 0; right: 0; }
  .brand-name {
    position: absolute;
    left: 60px;
    top: 128px;
    width: 190px;
    text-align: center;
    font-family: 'Montserrat', sans-serif;
    font-weight: 700;
    font-size: 25px;
    letter-spacing: 1px;
    line-height: 1;
  }
  .brand-name--red { color: var(--red); }
  .brand-name--grey { color: var(--grey); }
  .divider {
    position: absolute;
    left: 250px;
    top: 90px;
    width: 1px;
    height: 110px;
    background: var(--divider);
  }
  .person-name {
    position: absolute;
    left: 266px;
    top: 96px;
    margin: 0;
    font-family: 'Montserrat', sans-serif;
    font-weight: 700;
    font-size: 22px;
    color: var(--red);
    line-height: 1;
    letter-spacing: 0.5px;
  }
  .person-title {
    position: absolute;
    left: 266px;
    top: 122px;
    font-family: 'Roboto', sans-serif;
    font-size: 13px;
    color: var(--text);
  }
  .contact {
    position: absolute;
    left: 266px;
    display: flex;
    align-items: center;
    gap: 7px;
    font-family: 'Roboto', sans-serif;
    color: var(--text);
    line-height: 1;
  }
  .contact svg { width: 12px; height: 12px; flex: none; }
  .contact--phone { font-size: 15.5px; }
  .contact--email { font-size: 13.5px; }
  .card--person .contact--phone { top: 155px; }
  .card--person .contact--email { top: 175px; }
  .card--company .contact { left: 270px; }
  .card--company .contact--phone { top: 125px; }
  .card--company .contact--email { top: 145px; }
  .rule {
    position: absolute;
    left: 68px;
    top: 242px;
    width: 366px;
    height: 1px;
    background: linear-gradient(90deg, transparent, #6a6a6d 50%, transparent);
  }
  .company-name {
    position: absolute;
    left: 0;
    width: 100%;
    top: 256px;
    text-align: center;
    font-family: 'Montserrat', sans-serif;
    font-weight: 700;
    font-size: 12.5px;
    letter-spacing: 0.8px;
    color: var(--red);
    text-transform: uppercase;
  }
</style>
</head>
<body>
  <section class="card card--person">
    <span class="tab tab--top"></span>
    <span class="tab tab--bottom"></span>
    <div class="brand-name brand-name--red">STANBROOK</div>
    <span class="divider"></span>
    <h1 class="person-name">DANIEL HARTLEY</h1>
    <div class="person-title">Owner/ CEO</div>
    <div class="contact contact--phone">
      <svg viewBox="0 0 12 12" aria-hidden="true"><rect x="3" y="0.5" width="6" height="11" rx="1" fill="none" stroke="#e3212b" stroke-width="1.3"/><circle cx="6" cy="9.5" r="0.7" fill="#e3212b"/></svg>
      <span>08 6100 4270</span>
    </div>
    <div class="contact contact--email">
      <svg viewBox="0 0 12 12" aria-hidden="true"><rect x="0.5" y="2.5" width="11" height="7.5" fill="#e3212b"/><path d="M0.5 2.5 L6 7 L11.5 2.5" fill="none" stroke="#1b1b1d" stroke-width="1"/></svg>
      <span>dhartley@stanbrookfire.au</span>
    </div>
  </section>

  <section class="card card--company">
    <span class="tab tab--top"></span>
    <span class="tab tab--bottom"></span>
    <div class="brand-name brand-name--grey">STANBROOK</div>
    <span class="divider"></span>
    <div class="contact contact--phone">
      <svg viewBox="0 0 12 12" aria-hidden="true"><path d="M2.5 0.8 L4.6 3.3 L3.6 4.6 C4.3 6.1 5.9 7.7 7.4 8.4 L8.7 7.4 L11.2 9.5 L9.9 11.2 C5.5 11 1 6.5 0.8 2.1 Z" fill="#e3212b"/></svg>
      <span>08 6100 4270</span>
    </div>
    <div class="contact contact--email">
      <svg viewBox="0 0 12 12" aria-hidden="true"><rect x="0.5" y="2.5" width="11" height="7.5" fill="#e3212b"/><path d="M0.5 2.5 L6 7 L11.5 2.5" fill="none" stroke="#1b1b1d" stroke-width="1"/></svg>
      <span>office@stanbrookfire.au</span>
    </div>
    <span class="rule"></span>
    <div class="company-name">Stanbrook Fire Services Pty Ltd</div>
  </section>
</body>
</html>
```